Handy man Company business card

need branded business card for my new company, this design will transfer to car wrap design what winner will be asked to design

I will need original file so I can edit it in the end.

Also like to have some inspirational quote like "ONE CALL WE DO IT ALL"
"We do it right" can be added to logo side

Like to try to see large 1 800 000 0000 number on front with large logo

Size bigger then standard business card

I like to integrate LAS VEGAS sign to one of sides

Target Market(s)

Handy man services, Home renovation and remodeling

Industry/Entity Type

Handyman

Contact Information for Business Card

Tool Baron LLC.
Name: BORIS LENKOVA
Phone "Temporary": 000 000 0000
Adress: 2715 Fenmore Ct, Las Vegas NV 89147
Website: www.toolbaron.vegas
Email: info@toolbaron.vegas

Requirements
Must have
• Two side
• side n1: LOGO
• side n2: INFO
Nice to have
• Like to have some interesting idea for client to remember!
• With logo added to both side at different stile
Should not have
• Standard design,

```html
<!DOCTYPE html>
<html lang="en">
<head>
<meta charset="utf-8">
<title>Tool Baron LLC. — Business Card</title>
<link href="https://fonts.googleapis.com/css2?family=Open+Sans:wght@400;600;700&display=swap" rel="stylesheet">
<style>
  :root {
    --backdrop: #e9e7e3;
    --paper: #fbfbf9;
    --navy: #1c2d3a;
    --ink: #2a2f36;
    --muted: #7a7d80;
    --accent: #f0a324;
    --ghost-a: #eef0f1;
    --ghost-b: #dfe3e6;
  }
  * { box-sizing: border-box; margin: 0; padding: 0; }
  html, body {
    width: 1200px; height: 1200px; overflow: hidden;
    background: var(--backdrop);
    font-family: "Open Sans", Arial, sans-serif;
  }
  .sheet { position: relative; width: 1200px; height: 1200px; }
  .card {
    position: absolute; left: 180px; width: 840px; height: 480px;
    background: var(--paper); overflow: hidden;
    box-shadow: 0 6px 18px rgba(0,0,0,.15);
  }
  .card--info { top: 90px; }
  .card--brand { top: 630px; }
  .card__shape { position: absolute; inset: 0; width: 100%; height: 100%; }

  .brandmark { position: absolute; display: flex; align-items: center; gap: 14px; }
  .brandmark__dot { width: 30px; height: 30px; border-radius: 50%; background: var(--accent); }
  .brandmark__name { font-weight: 700; color: var(--navy); white-space: nowrap; }
  .card--info .brandmark { left: 330px; top: 110px; }
  .card--info .brandmark__name { font-size: 46px; }
  .card--brand .brandmark { right: 70px; bottom: 70px; }
  .card--brand .brandmark__dot { width: 22px; height: 22px; }
  .card--brand .brandmark__name { font-size: 32px; }

  .holder {
    position: absolute; left: 160px; top: 262px;
    font-size: 19px; letter-spacing: 1.5px; color: var(--muted);
  }
  .contacts { position: absolute; left: 160px; top: 312px; list-style: none; }
  .contacts li {
    display: flex; align-items: center; gap: 14px;
    font-size: 17px; color: var(--ink); line-height: 30px;
  }
  .contacts__icon {
    width: 16px; height: 16px; background: var(--accent); flex: none;
    display: flex; align-items: center; justify-content: center;
  }

  .mascot-area {
    position: absolute; left: 70px; top: -40px; width: 420px; height: 300px;
    border-radius: 50%;
    background: radial-gradient(ellipse at center, var(--ghost-b), var(--ghost-a) 70%, transparent 72%);
  }
</style>
</head>
<body>
<main class="sheet">

  <section class="card card--info" aria-label="Contact side">
    <svg class="card__shape" viewBox="0 0 840 480" aria-hidden="true">
      <rect width="840" height="480" fill="var(--navy)"/>
      <path d="M130 0 L710 0 Q880 240 710 480 L130 480 Q-40 240 130 0 Z" fill="var(--paper)"/>
    </svg>
    <div class="brandmark">
      <span class="brandmark__dot"></span>
      <span class="brandmark__name">Tool Baron</span>
    </div>
    <p class="holder">BORIS LENKOVA</p>
    <ul class="contacts">
      <li>
        <span class="contacts__icon">
          <svg width="10" height="10" viewBox="0 0 10 10"><path d="M2 1 L4 1 L4.5 3 L3.3 4 Q4.5 6 6 6.7 L7 5.5 L9 6 L9 8 Q5 9 1 4 Q1 2 2 1Z" fill="#fff"/></svg>
        </span>000 000 0000
      </li>
      <li>
        <span class="contacts__icon">
          <svg width="10" height="10" viewBox="0 0 10 10"><circle cx="5" cy="5" r="3.8" fill="none" stroke="#fff" stroke-width="1.2"/><path d="M1.2 5 H8.8 M5 1.2 V8.8" stroke="#fff" stroke-width="1"/></svg>
        </span>www.toolbaron.vegas
      </li>
      <li>
        <span class="contacts__icon">
          <svg width="10" height="10" viewBox="0 0 10 10"><rect x="1" y="2.5" width="8" height="5.5" fill="none" stroke="#fff" stroke-width="1.1"/><path d="M1 2.5 L5 5.5 L9 2.5" fill="none" stroke="#fff" stroke-width="1.1"/></svg>
        </span>info@toolbaron.vegas
      </li>
      <li>
        <span class="contacts__icon">
          <svg width="10" height="10" viewBox="0 0 10 10"><path d="M5 9 Q1.5 5 1.5 3.7 A3.5 3.5 0 0 1 8.5 3.7 Q8.5 5 5 9Z" fill="#fff"/><circle cx="5" cy="3.7" r="1.2" fill="var(--accent)"/></svg>
        </span>2715 Fenmore Ct, Las Vegas NV 89147
      </li>
    </ul>
  </section>

  <section class="card card--brand" aria-label="Logo side">
    <div class="mascot-area" role="img" aria-label="Large faint mascot illustration of a handyman giving a thumbs up"></div>
    <div class="brandmark">
      <span class="brandmark__dot"></span>
      <span class="brandmark__name">Tool Baron</span>
    </div>
  </section>

</main>
</body>
</html>
```